Lawyers in the Netherlands website + logo

We are going in 2015 to launch a website where all law firms in the Netherlands and have the opportunity to place an ad program.

The domain name wil be:

kantoorvinder.website

We want a responsive PSD bootstrap twitter 1170 pixel grid.
for the homepage, result page and the detail page of the customer.

This sites we like:
https://www.qorvantis.com/lawyers

https://lawyers.qorvantis.com/lawyer/tim-garsby-7305826

http://solicitordirectory.brevimark.co.uk/
Map of the Netherlands?

http://solicitordirectory.brevimark.co.uk/listing/category-search/commercial
http://www.tandelvo.com.au/find-a-lawyer/banking-finance-law/

```html
<!DOCTYPE html>
<html lang="en">
<head>
<meta charset="utf-8">
<title>Kantoorvinder – Find a Lawyer</title>
<link rel="stylesheet" href="https://fonts.googleapis.com/css2?family=Source+Sans+3:wght@300;400;600;700&display=swap">
<style>
:root{
  --red:#d5141c;
  --red-deep:#8f1520;
  --band-red:#9a1a24;
  --ink:#1b1b1b;
  --box:#232323;
  --box-line:#3a3a3a;
  --text:#333;
  --muted:#777;
  --white:#fff;
  --yellow:#f4c20d;
  --grey-btn:#555;
}
*{box-sizing:border-box;margin:0;padding:0}
html,body{width:1200px;height:3740px;overflow:hidden}
body{font-family:"Source Sans 3",Arial,sans-serif;color:var(--text);background:var(--white);position:relative}
ul{list-style:none}
.container{width:880px;margin:0 auto;position:relative;height:100%}

/* top bar */
.topbar{height:24px;background:#111;color:#ddd;font-size:11px}
.topbar .container{display:flex;align-items:center;justify-content:space-between}
.topbar nav{display:flex;gap:22px}
.topbar .left a{color:#ddd}
.topbar .right a{color:var(--white)}
.topbar a{text-decoration:none}

/* header */
.site-header{height:64px;background:var(--ink)}
.site-header .container{display:flex;align-items:center;justify-content:space-between}
.brand{color:var(--white);font-weight:700;font-size:24px;letter-spacing:.5px}
.header-actions{display:flex;gap:10px}
.btn{display:inline-block;font-size:11px;font-weight:700;color:var(--white);padding:6px 14px;border-radius:2px;text-transform:uppercase}
.btn-red{background:var(--red)}
.btn-grey{background:var(--grey-btn)}

/* hero */
.hero{height:412px;background:linear-gradient(135deg,#dcdfe3 0%,#b9bec6 40%,#8d95a0 70%,#c9ccd1 100%)}

/* search */
.search-bar{height:92px;background:var(--red)}
.search-bar .container{display:flex;align-items:center;gap:14px}
.search-tag{color:var(--white);font-weight:700;font-size:15px;line-height:1.2;text-transform:uppercase;width:240px;padding-left:28px;position:relative}
.search-tag svg{position:absolute;left:0;top:-6px}
.field{background:var(--white);height:34px;font-size:12px;color:#999;display:flex;align-items:center;padding:0 10px}
.field-issue{width:240px}
.field-place{width:220px}
.btn-search{background:var(--yellow);color:#222;font-weight:700;font-size:15px;height:34px;padding:0 16px;display:flex;align-items:center}

/* section headings */
.section-kicker{font-size:15px;color:#444}
.section-title{font-size:28px;font-weight:700;color:var(--red);line-height:1;text-transform:uppercase}

/* practice area */
.practice{height:764px;padding-top:44px}
.practice-grid{display:grid;grid-template-columns:repeat(3,276px);column-gap:26px;row-gap:14px;margin-top:18px}
.practice-box{background:var(--box);padding:8px 12px}
.practice-box li{color:#eee;font-size:13px;line-height:30px;border-bottom:1px solid var(--box-line);padding-left:14px;position:relative}
.practice-box li:last-child{border-bottom:0}
.practice-box li::before{content:"";position:absolute;left:2px;top:13px;width:4px;height:4px;background:#bbb}
.row-short{height:228px}
.row-long{height:375px}

/* promo bands */
.band{height:296px;background:linear-gradient(180deg,#a1202a 0%,var(--band-red) 50%,#7e141d 100%);display:flex;flex-direction:column;align-items:center;justify-content:center;color:var(--white);text-transform:uppercase;text-align:center}
.band-line1{font-size:26px;font-weight:300;letter-spacing:.5px}
.band-line2{font-size:31px;font-weight:700;letter-spacing:.5px;margin-top:4px}

/* lists */
.link-list li{font-size:13px;color:#333;line-height:24px;padding-left:12px;position:relative}
.link-list li::before{content:"›";position:absolute;left:0;color:var(--red);font-weight:700}

.states{height:456px;padding-top:48px;position:relative}
.states .world-map{position:absolute;left:330px;top:28px;width:560px;height:330px;background:radial-gradient(ellipse at center,#eef0f2 0%,#f6f7f8 60%,rgba(255,255,255,0) 75%)}
.state-cols{display:grid;grid-template-columns:repeat(4,228px);margin-top:14px;position:relative}

.cities{height:640px;padding-top:56px}
.city-top{display:grid;grid-template-columns:repeat(3,300px);margin-top:16px}
.city-top li{line-height:18px}
.city-cols{display:grid;grid-template-columns:repeat(3,300px);margin-top:20px}

/* directory */
.directory{height:354px;background:var(--red-deep)}
.directory .container{display:grid;grid-template-columns:repeat(3,1fr);gap:40px;padding-top:42px}
.dir-item{text-align:center;color:var(--white)}
.circle{width:76px;height:76px;border-radius:50%;margin:0 auto 12px;display:flex;align-items:center;justify-content:center}
.circle-light{background:var(--white)}
.dir-brand{font-size:12px;text-transform:uppercase;letter-spacing:.5px}
.dir-title{font-size:19px;font-weight:700;text-transform:uppercase;line-height:1.1}
.dir-text{font-size:12px;line-height:1.45;margin-top:10px;padding:0 10px;color:#f2dcdc}

/* free info */
.info{height:305px;background:linear-gradient(180deg,#2a2c30 0%,#1c1d20 60%,#15161a 100%);color:var(--white);text-align:center;padding-top:40px}
.info-kicker{font-size:15px;color:#ddd}
.info-title{font-size:21px;font-weight:700;text-transform:uppercase;line-height:1.3;margin-top:4px}
.info-items{display:grid;grid-template-columns:repeat(3,1fr);width:880px;margin:26px auto 0}
.circle-dark{background:#555;border:3px solid #888}
.info-label{font-size:17px;font-weight:700;text-transform:uppercase}

/* footer */
.site-footer{height:37px;background:#0e0e0e;color:#aaa;font-size:11px}
.site-footer .container{display:flex;align-items:center;justify-content:space-between}
.site-footer nav{display:flex;gap:18px}
</style>
</head>
<body>

<div class="topbar">
  <div class="container">
    <nav class="left"><a href="#">Find a Lawyer</a><a href="#">Legal Answers</a><a href="#">Law</a><a href="#">More ▾</a></nav>
    <nav class="right"><a href="#">Sign In</a><a href="#">Lawyers Get Listed</a><a href="#">FAQ</a></nav>
  </div>
</div>

<header class="site-header">
  <div class="container">
    <div class="brand">Kantoorvinder</div>
    <div class="header-actions"><span class="btn btn-red">Sign In</span><span class="btn btn-grey">Lawyers Get Listed</span></div>
  </div>
</header>

<section class="hero" role="img" aria-label="Photo of three lawyers smiling around a laptop in an office"></section>

<section class="search-bar">
  <div class="container">
    <div class="search-tag">
      <svg width="22" height="20" viewBox="0 0 22 20"><path d="M2 18 C4 8 10 4 18 4" fill="none" stroke="#fff" stroke-width="2"/><path d="M14 1 L19 4 L15 8" fill="none" stroke="#fff" stroke-width="2"/></svg>
      Helping you<br>with your legal needs
    </div>
    <div class="field field-issue">Search Legal Issue or Lawyer Name</div>
    <div class="field field-place">City, State or Zip Code</div>
    <div class="btn-search">SEARCH NOW</div>
  </div>
</section>

<section class="practice">
  <div class="container">
    <p class="section-kicker">Find Lawyers by</p>
    <h2 class="section-title">Practice Area</h2>
    <div class="practice-grid">
      <ul class="practice-box row-short"><li>Bankruptcy</li><li>Business Law</li><li>Consumer Law</li><li>Criminal Law</li><li>Divorce</li><li>DUI &amp; DWI</li><li>Employment Law</li></ul>
      <ul class="practice-box row-short"><li>Estate Planning</li><li>Family Law</li><li>Foreclosure Defense</li><li>Immigration Law</li><li>Intellectual Property</li><li>Medical Malpractice</li><li>Nursing Home Abuse &amp; Neglect</li></ul>
      <ul class="practice-box row-short"><li>Personal Injury</li><li>Probate</li><li>Products Liability</li><li>Real Estate Law</li><li>Tax Law</li><li>Traffic Tickets</li><li>Workers' Compensation</li></ul>
      <ul class="practice-box row-long"><li>Agricultural Law</li><li>Animal &amp; Dog Law</li><li>Antitrust</li><li>Appeals &amp; Appellate</li><li>Arbitration &amp; Mediation</li><li>Asbestos &amp; Mesothelioma</li><li>Broker Fraud</li><li>Civil Rights</li><li>Collections</li><li>Communications &amp; Internet Law</li><li>Construction Law</li><li>Domestic Violence</li></ul>
      <ul class="practice-box row-long"><li>Education Law</li><li>Elder Law</li><li>Energy, Oil and Gas</li><li>Entertainment &amp; Sports</li><li>Environmental Law</li><li>Gov &amp; Administrative Law</li><li>Health Care Law</li><li>Insurance Claims</li><li>Insurance Defense</li><li>International Law</li><li>Juvenile Law</li></ul>
      <ul class="practice-box row-long"><li>Landlord Tenant</li><li>Legal Malpractice</li><li>Maritime</li><li>Military Law</li><li>Municipal Law</li><li>Native American Law</li><li>Patents</li><li>Securities Law</li><li>Social Security Disability/SSI</li><li>Trademarks</li><li>White Collar Crime</li></ul>
    </div>
  </div>
</section>

<section class="band" role="img" aria-label="City buildings photo under a red overlay">
  <p class="band-line1">Lorem Ipsum is simply</p>
  <p class="band-line2">Dummy text of the printing and typesetting</p>
</section>

<section class="states">
  <div class="container">
    <div class="world-map" role="img" aria-label="Faint world map in the background"></div>
    <p class="section-kicker">Find Lawyers by</p>
    <h2 class="section-title">State</h2>
    <div class="state-cols">
      <ul class="link-list"><li>Alabama</li><li>Alaska</li><li>Arizona</li><li>Arkansas</li><li>California</li><li>Colorado</li><li>Connecticut</li><li>Delaware</li><li>Florida</li><li>Georgia</li><li>Hawaii</li><li>Idaho</li><li>Illinois</li></ul>
      <ul class="link-list"><li>Indiana</li><li>Iowa</li><li>Kansas</li><li>Kentucky</li><li>Louisiana</li><li>Maine</li><li>Maryland</li><li>Massachusetts</li><li>Michigan</li><li>Minnesota</li><li>Mississippi</li><li>Missouri</li><li>Montana</li></ul>
      <ul class="link-list"><li>Nebraska</li><li>Nevada</li><li>New Hampshire</li><li>New Jersey</li><li>New Mexico</li><li>New York</li><li>North Carolina</li><li>North Dakota</li><li>Ohio</li><li>Oklahoma</li><li>Oregon</li><li>Pennsylvania</li><li>Rhode Island</li></ul>
      <ul class="link-list"><li>South Carolina</li><li>South Dakota</li><li>Tennessee</li><li>Texas</li><li>Utah</li><li>Vermont</li><li>Virginia</li><li>Washington</li><li>West Virginia</li><li>Wisconsin</li><li>Wyoming</li><li>Washington, DC</li></ul>
    </div>
  </div>
</section>

<section class="band" role="img" aria-label="Courthouse columns photo under a red overlay">
  <p class="band-line1">Lorem Ipsum is simply</p>
  <p class="band-line2">Dummy text of the printing and typesetting</p>
</section>

<section class="cities">
  <div class="container">
    <p class="section-kicker">Find Lawyers by</p>
    <h2 class="section-title">City</h2>
    <div class="city-top">
      <ul class="link-list"><li>Chicago</li><li>Dallas</li></ul>
      <ul class="link-list"><li>Houston</li><li>Los Angeles</li></ul>
      <ul class="link-list"><li>New York City</li><li>Washington, DC</li></ul>
    </div>
    <div class="city-cols">
      <ul class="link-list"><li>Albuquerque</li><li>Atlanta</li><li>Austin</li><li>Baltimore</li><li>Birmingham</li><li>Boston</li><li>Charlotte</li><li>Chicago</li><li>Cincinnati</li><li>Cleveland</li><li>Columbus</li><li>Dallas</li><li>Denver</li><li>Detroit</li><li>Fort Worth</li><li>Hartford</li><li>Honolulu</li></ul>
      <ul class="link-list"><li>Houston</li><li>Indianapolis</li><li>Jacksonville</li><li>Kansas City, MO</li><li>Las Vegas</li><li>Los Angeles</li><li>Louisville</li><li>Memphis</li><li>Miami</li><li>Milwaukee</li><li>Minneapolis</li><li>Nashville</li><li>New Orleans</li><li>New York City</li><li>Oklahoma City</li><li>Orlando</li><li>Philadelphia</li></ul>
      <ul class="link-list"><li>Phoenix</li><li>Pittsburgh</li><li>Portland</li><li>Providence</li><li>Raleigh</li><li>Richmond</li><li>Riverside</li><li>Sacramento</li><li>Saint Louis</li><li>Salt Lake City</li><li>San Antonio</li><li>San Diego</li><li>San Francisco</li><li>San Jose</li><li>Seattle</li><li>Tampa</li><li>Washington, DC</li></ul>
    </div>
  </div>
</section>

<section class="directory">
  <div class="container">
    <div class="dir-item">
      <div class="circle circle-light"><svg width="36" height="28" viewBox="0 0 36 28"><path d="M2 12 L10 6 L18 10 L26 6 L34 12 L24 22 L18 18 L12 22 Z" fill="#8f1520"/></svg></div>
      <p class="dir-brand">Kantoorvinder</p>
      <p class="dir-title">Lawyer Directory</p>
      <p class="dir-text">Lorem Ipsum is simply dummy text of the printing and typesetting industry Lorem Ipsum has been the industry's standard dummy text.</p>
    </div>
    <div class="dir-item">
      <div class="circle circle-light"><svg width="36" height="28" viewBox="0 0 36 28"><path d="M2 12 L10 6 L18 10 L26 6 L34 12 L24 22 L18 18 L12 22 Z" fill="#8f1520"/></svg></div>
      <p class="dir-brand">Kantoorvinder</p>
      <p class="dir-title">Lawyer Directory</p>
      <p class="dir-text">Lorem Ipsum is simply dummy text of the printing and typesetting industry Lorem Ipsum has been the industry's standard dummy text.</p>
    </div>
    <div class="dir-item">
      <div class="circle circle-light"><svg width="36" height="28" viewBox="0 0 36 28"><path d="M2 12 L10 6 L18 10 L26 6 L34 12 L24 22 L18 18 L12 22 Z" fill="#8f1520"/></svg></div>
      <p class="dir-brand">Kantoorvinder</p>
      <p class="dir-title">Lawyer Directory</p>
      <p class="dir-text">Lorem Ipsum is simply dummy text of the printing and typesetting industry Lorem Ipsum has been the industry's standard dummy text.</p>
    </div>
  </div>
</section>

<section class="info" role="img" aria-label="Dark city skyline photo behind the free legal information block">
  <p class="info-kicker">Free Legal Information on Kantoorvinder</p>
  <h2 class="info-title">Can help you make an educated decision<br>when hiring an attorney</h2>
  <div class="info-items">
    <div>
      <div class="circle circle-dark"><svg width="32" height="28" viewBox="0 0 32 28"><path d="M3 3 H29 V19 H14 L7 25 V19 H3 Z" fill="none" stroke="#fff" stroke-width="2.5"/></svg></div>
      <p class="info-label">Questions &amp; Answers</p>
    </div>
    <div>
      <div class="circle circle-dark"><svg width="32" height="30" viewBox="0 0 32 30"><path d="M2 10 L16 2 L30 10 Z M5 12 V24 M12 12 V24 M20 12 V24 M27 12 V24 M2 27 H30" fill="none" stroke="#fff" stroke-width="2.5"/></svg></div>
      <p class="info-label">Legal Practice Centers</p>
    </div>
    <div>
      <div class="circle circle-dark"><svg width="26" height="30" viewBox="0 0 26 30"><path d="M3 2 H17 L23 8 V28 H3 Z M8 14 H18 M8 19 H18 M8 24 H15" fill="none" stroke="#fff" stroke-width="2.5"/></svg></div>
      <p class="info-label">Codes, Regulations &amp; Case Law</p>
    </div>
  </div>
</section>

<footer class="site-footer">
  <div class="container">
    <p>© Copyright 2015 Kantoorvinder</p>
    <nav><span>Company</span><span>Terms of Service</span><span>Privacy Policy</span><span>Contact Us</span></nav>
  </div>
</footer>

</body>
</html>
```